Criação de Embalagem (família até 5 unid.) para Alimentos & Bebidas
A empresa queria:
" A Frutolla é uma loja que comercializa as frutas vermelhas que produz e produtos feitos com as frutas, como: vinagres de framboesa e amora, geleias, granolas, cookies, cosméticos, bolos, tortas, doces, frutas(berries) congeladas, frutas desidratadas, caldas etc. Os produtos sao naturais e as frutas orgânicas. Nossa proposta é uma loja que leva as propriedades das frutas vermelhas para o dia a dia dos clientes, propiciando uma vida mais saudável, gostosa e inovadora. "

```html
<!DOCTYPE html>
<html lang="pt-BR">
<head>
<meta charset="utf-8">
<title>Frutolla Granola Frutas Vermelhas – Rótulo</title>
<link href="https://fonts.googleapis.com/css2?family=Great+Vibes&family=Amatic+SC:wght@700&family=Open+Sans:wght@400;600;700&family=Open+Sans+Condensed:wght@700&display=swap" rel="stylesheet">
<style>
  :root {
    --backdrop: #8d8e86;
    --backdrop-edge: #6f706a;
    --label-cream: #f5eed8;
    --label-cream-deep: #e9dfc2;
    --ink-brown: #4b2a22;
    --ink-soft: #6b4a3e;
    --line-brown: #5a3a30;
    --berry-red: #c8283a;
    --berry-dark: #2d1c26;
    --leaf-green: #4f8a3a;
  }
  html, body {
    margin: 0;
    width: 1200px;
    height: 1200px;
    overflow: hidden;
  }
  body {
    background: radial-gradient(circle at 50% 45%, var(--backdrop) 55%, var(--backdrop-edge) 100%);
    font-family: "Open Sans", sans-serif;
    position: relative;
  }
  .label {
    position: absolute;
    left: 211px;
    top: 19px;
    width: 778px;
    height: 1157px;
    background: linear-gradient(180deg, var(--label-cream) 0%, var(--label-cream) 60%, var(--label-cream-deep) 100%);
    box-shadow: 0 6px 24px rgba(0,0,0,0.35);
    overflow: hidden;
  }
  .frame-lines {
    position: absolute;
    inset: 0;
  }
  .brand-name {
    position: absolute;
    top: 70px;
    left: 0;
    right: 0;
    text-align: center;
    font-family: "Open Sans", sans-serif;
    font-weight: 700;
    font-size: 66px;
    letter-spacing: 3px;
    color: var(--ink-brown);
    margin: 0;
  }
  .product-name {
    position: absolute;
    top: 300px;
    left: 0;
    right: 0;
    text-align: center;
    font-family: "Great Vibes", cursive;
    font-size: 190px;
    line-height: 1;
    color: var(--ink-brown);
    margin: 0;
  }
  .flavour-arc {
    position: absolute;
    left: 0;
    top: 500px;
    width: 778px;
    height: 160px;
  }
  .flavour-arc text {
    font-family: "Amatic SC", cursive;
    font-size: 46px;
    letter-spacing: 4px;
    fill: var(--ink-brown);
  }
  .origin-note {
    position: absolute;
    left: 20px;
    top: 640px;
    width: 250px;
    text-align: center;
    font-size: 22px;
    line-height: 1.3;
    color: var(--ink-soft);
    margin: 0;
  }
  .claim-badge {
    position: absolute;
    left: 593px;
    top: 598px;
    width: 168px;
    height: 168px;
    border-radius: 50%;
    background: var(--ink-brown);
    color: var(--label-cream);
    display: flex;
    align-items: center;
    justify-content: center;
    text-align: center;
    font-family: "Open Sans Condensed", "Open Sans", sans-serif;
    font-weight: 700;
    font-size: 25px;
    line-height: 1.15;
  }
  .claim-badge::before {
    content: "";
    position: absolute;
    inset: 8px;
    border: 2px solid var(--label-cream);
    border-radius: 50%;
  }
  .berries-photo {
    position: absolute;
    left: 0;
    top: 770px;
    width: 778px;
    height: 325px;
    background:
      radial-gradient(ellipse at 25% 55%, var(--berry-red) 0%, transparent 40%),
      radial-gradient(ellipse at 70% 60%, var(--berry-red) 0%, transparent 40%),
      radial-gradient(ellipse at 45% 30%, var(--leaf-green) 0%, transparent 30%),
      radial-gradient(ellipse at 50% 75%, var(--berry-dark) 0%, transparent 45%),
      linear-gradient(180deg, rgba(245,238,216,0) 0%, #8a2a33 45%, #5a2230 100%);
    -webkit-mask-image: linear-gradient(180deg, transparent 0%, #000 25%, #000 85%, transparent 100%);
    mask-image: linear-gradient(180deg, transparent 0%, #000 25%, #000 85%, transparent 100%);
  }
  .net-weight {
    position: absolute;
    left: 0;
    right: 0;
    top: 1092px;
    text-align: center;
    font-size: 36px;
    font-weight: 400;
    color: var(--ink-brown);
    margin: 0;
  }
</style>
</head>
<body>
  <main class="label">
    <svg class="frame-lines" width="778" height="1157" viewBox="0 0 778 1157" aria-hidden="true">
      <g fill="none" stroke="var(--line-brown)" stroke-width="2.5">
        <path d="M26 160 V26 H160"/>
        <path d="M38 150 V38 H150"/>
        <path d="M752 160 V26 H618"/>
        <path d="M740 150 V38 H628"/>
        <path d="M170 265 Q389 220 608 265"/>
        <path d="M230 285 H548"/>
        <path d="M190 520 Q389 555 588 520"/>
        <path d="M130 500 H260"/>
        <path d="M518 500 H648"/>
      </g>
    </svg>

    <h1 class="brand-name">Frutolla</h1>

    <h2 class="product-name">Granola</h2>

    <svg class="flavour-arc" viewBox="0 0 778 160" aria-label="Frutas vermelhas">
      <path id="flavour-curve" d="M210 40 Q389 130 568 40" fill="none"/>
      <text text-anchor="middle"><textPath href="#flavour-curve" startOffset="50%">-FRUTAS VERMELHAS-</textPath></text>
    </svg>

    <p class="origin-note">Uma receita tradicional de família 100% natural produzido na Serra da Mantiqueira</p>

    <div class="claim-badge">RICO EM<br>FIBRAS E<br>PROTEÍNAS</div>

    <div class="berries-photo" role="img" aria-label="Fotografia de framboesas, amoras e mirtilos com folhas verdes"></div>

    <p class="net-weight">200 g</p>
  </main>
</body>
</html>
```